Visitenkarten-Design für Premiumstahlhandel
Vielen Dank für die tollen und vielfältigen Designvorschläge. Unsere Änderungswünsche wurden schnell umgesetzt und auf Fragen wurde immer schnell geantwortet. Wir können tolvir absolut weiterempfehlen.
Zielgruppe
Wir sind ein Premiumstahlhandel mit breitem Sortiment und modernem Lager- und Logistikzentrum. Unsere Zielgruppe sind regionale und überregionale Industrieunternehmen, die Wert auf Qualität und Service legen.
Aufgabenstellung
Bitte Vorder- und Rückseite designen im Querformat (8,7x5,7 mit Beschnitt / Endmaß 8,5x5,5 cm) Bis jetzt haben wir auf den Visitenkarten auf der Rückseite einen QR Code mit allen Daten der Visitenkarte angebracht. (siehe Beispiel) Die Schrift des Logos könnte man auch in Weiß machen und die Rauten Orange, wenn es der Hintergrund notwendig macht. Der Slogan Wir können Stahl. könnte auch nur als Schrift ohne Rahmen auf der Visitenkarte stehen.

```html
<!DOCTYPE html>
<html lang="de">
<head>
<meta charset="utf-8">
<title>Halden Stahl – Visitenkarte</title>
<link href="https://fonts.googleapis.com/css2?family=Open+Sans:wght@400;600;700&display=swap" rel="stylesheet">
<style>
  :root {
    --navy: #1c2f4d;
    --navy-soft: #243a5c;
    --orange: #e2701f;
    --paper: #f2f2f2;
    --ground: #d8d6d7;
    --white: #ffffff;
    --ink: #1b1b1b;
  }
  * { margin: 0; padding: 0; box-sizing: border-box; }
  html, body { width: 1200px; height: 900px; overflow: hidden; }
  body {
    background: var(--ground);
    font-family: "Open Sans", Arial, sans-serif;
    position: relative;
  }
  .card {
    position: absolute;
    left: 320px;
    width: 560px;
    height: 362px;
    overflow: hidden;
    box-shadow: 0 6px 18px rgba(0,0,0,0.25);
  }
  .card--front { top: 50px; background: var(--navy); }
  .card--back { top: 488px; background: var(--navy); }

  /* Front */
  .front__top {
    position: absolute; left: 0; top: 0; width: 100%; height: 205px;
    background: linear-gradient(180deg, #e4e4e4 0%, var(--paper) 100%);
  }
  .brand {
    position: absolute; display: flex; align-items: center; gap: 14px;
  }
  .brand__square { background: var(--orange); display: block; }
  .brand__name { font-weight: 700; letter-spacing: 1px; text-transform: uppercase; }
  .front__brand { left: 56px; top: 52px; }
  .front__brand .brand__square { width: 42px; height: 42px; }
  .front__brand .brand__name { font-size: 42px; color: var(--navy); }

  .person { position: absolute; left: 180px; top: 118px; color: var(--ink); }
  .person__name { font-size: 24px; letter-spacing: 1px; font-weight: 400; }
  .person__name strong { font-weight: 700; }
  .person__role { font-size: 11px; letter-spacing: 1.5px; margin-left: 96px; margin-top: -2px; }

  .company-band {
    position: absolute; left: 150px; top: 192px; width: 300px; height: 28px;
    background: var(--orange); color: var(--white);
    font-size: 17px; font-weight: 600; letter-spacing: 1px;
    display: flex; align-items: center; justify-content: center;
  }

  .contact {
    position: absolute; color: var(--white); font-size: 11.5px; line-height: 1.35;
    display: flex; align-items: flex-start; gap: 10px;
  }
  .contact__icon { width: 16px; height: 16px; margin-top: 6px; fill: var(--white); }
  .contact__rule { width: 2px; height: 24px; background: var(--white); margin-top: 2px; }
  .contact__extra { display: block; margin-top: 10px; margin-left: 8px; }
  .contact--phone { left: 40px; top: 262px; }
  .contact--address { left: 330px; top: 238px; }

  /* Back */
  .back__brand { left: 0; right: 0; top: 120px; justify-content: center; }
  .back__brand .brand__square { width: 46px; height: 46px; }
  .back__brand .brand__name { font-size: 46px; color: var(--white); }
  .slogan {
    position: absolute; left: 30px; right: 30px; top: 250px;
    display: flex; align-items: center; gap: 18px; color: var(--white);
  }
  .slogan__rule { flex: 1; height: 2px; background: rgba(255,255,255,0.85); }
  .slogan__text { font-size: 20px; font-weight: 600; letter-spacing: 0.5px; white-space: nowrap; }
</style>
</head>
<body>

<section class="card card--front" aria-label="Vorderseite">
  <div class="front__top"></div>
  <div class="brand front__brand">
    <span class="brand__square"></span>
    <span class="brand__name">Halden Stahl</span>
  </div>
  <div class="person">
    <p class="person__name">JONAS <strong>BEISPIEL</strong></p>
    <p class="person__role">GESCHÄFTSFÜHRER</p>
  </div>
  <div class="company-band">Halden Stahl GmbH</div>

  <div class="contact contact--phone">
    <svg class="contact__icon" viewBox="0 0 24 24" aria-hidden="true"><path d="M6.6 10.8a15.1 15.1 0 0 0 6.6 6.6l2.2-2.2a1 1 0 0 1 1-.25 11.4 11.4 0 0 0 3.6.57 1 1 0 0 1 1 1V20a1 1 0 0 1-1 1A17 17 0 0 1 3 4a1 1 0 0 1 1-1h3.5a1 1 0 0 1 1 1c0 1.25.2 2.45.57 3.57a1 1 0 0 1-.25 1z"/></svg>
    <span class="contact__rule"></span>
    <p>Tel: + 49 (0)700 / 00-000<br>M: +49 (0)170 / 000 000 00
      <span class="contact__extra">mailadresse.name@halden-stahl.de</span></p>
  </div>

  <div class="contact contact--address">
    <svg class="contact__icon" viewBox="0 0 24 24" aria-hidden="true"><path d="M12 3 2 12h3v8h5v-5h4v5h5v-8h3z"/></svg>
    <span class="contact__rule"></span>
    <p>Werkstraße 12<br>D-70000 Neustadt a.F.
      <span class="contact__extra">www.halden-stahl.de</span></p>
  </div>
</section>

<section class="card card--back" aria-label="Rückseite">
  <div class="brand back__brand">
    <span class="brand__square"></span>
    <span class="brand__name">Halden Stahl</span>
  </div>
  <div class="slogan">
    <span class="slogan__rule"></span>
    <span class="slogan__text">Wir können Stahl</span>
    <span class="slogan__rule"></span>
  </div>
</section>

</body>
</html>
```